Letterhead

Can you please design me a letterhead that I can use electronically in word as a template. I have attached my business card as I would like the design to reflect this logo.

```html
<!DOCTYPE html>
<html lang="en">
<head>
<meta charset="utf-8">
<title>Kestrel Business Consultants – Letterhead</title>
<link rel="stylesheet" href="https://fonts.googleapis.com/css2?family=Open+Sans:wght@400;700;800&display=swap">
<style>
  :root {
    --bg: #ececec;
    --paper: #ffffff;
    --brand-red: #a8242a;
    --brand-black: #1c1a1a;
    --ink: #3a3a3a;
    --watermark: #f1f1ef;
  }
  * { box-sizing: border-box; margin: 0; padding: 0; }
  html, body {
    width: 1200px;
    height: 950px;
    overflow: hidden;
    background: var(--bg);
    font-family: "Open Sans", Arial, sans-serif;
  }
  .canvas {
    width: 1200px;
    height: 950px;
    display: flex;
    align-items: center;
    justify-content: center;
  }
  .letterhead {
    position: relative;
    width: 630px;
    height: 890px;
    background: var(--paper);
    box-shadow: 0 4px 18px rgba(0,0,0,0.12);
    overflow: hidden;
  }
  .band {
    position: absolute;
    left: 0;
    width: 100%;
    height: 9px;
    display: flex;
  }
  .band--top { top: 0; }
  .band--bottom { bottom: 0; flex-direction: row-reverse; }
  .band__accent { width: 58px; background: var(--brand-black); }
  .band__main { flex: 1; background: var(--brand-red); }

  .brand {
    position: absolute;
    top: 30px;
    left: 34px;
  }
  .brand__name {
    font-weight: 800;
    font-size: 40px;
    line-height: 1;
    letter-spacing: -0.5px;
    color: var(--brand-red);
  }
  .brand__tagline {
    margin-top: 3px;
    margin-left: 20px;
    font-size: 8.5px;
    color: var(--ink);
  }

  .contact {
    position: absolute;
    top: 30px;
    right: 46px;
    list-style: none;
    font-size: 10.5px;
    line-height: 1.35;
    color: var(--ink);
  }
  .contact__label { color: var(--brand-red); }

  .watermark {
    position: absolute;
    top: 430px;
    left: 50%;
    transform: translate(-50%, -50%) rotate(-32deg);
    font-weight: 800;
    font-size: 130px;
    letter-spacing: -2px;
    color: var(--watermark);
    white-space: nowrap;
    user-select: none;
  }
</style>
</head>
<body>
<main class="canvas">
  <article class="letterhead">
    <div class="band band--top">
      <span class="band__accent"></span>
      <span class="band__main"></span>
    </div>

    <header class="brand">
      <div class="brand__name">kestrel</div>
      <div class="brand__tagline">Business Consultants Pty Ltd</div>
    </header>

    <ul class="contact">
      <li><span class="contact__label">P</span> : 0400 512 384</li>
      <li><span class="contact__label">E</span> : claire@kestrel.net.au</li>
      <li><span class="contact__label">ACN</span> : 061 428 735</li>
    </ul>

    <div class="watermark" aria-hidden="true">kestrel</div>

    <div class="band band--bottom">
      <span class="band__accent"></span>
      <span class="band__main"></span>
    </div>
  </article>
</main>
</body>
</html>
```